Add Responsiveness to Current Website

The website http://www.quillbrook-sound-rooms.example needs to be made responsive. This includes all the menus and all the galleries. The Design, graphics, colors can remain the same, except I can provide larger images and design for the Home Page. If you know what you are doing, this should not take too long.

Coding

Coded - Design and coding required

Number of Pages Required

5+ page

Font styles to use
Sans Serif

Colors
f37122
f78f20

Requirements
Must have
• Responsive Menus and Galleries

```html
<!DOCTYPE html>
<html lang="en">
<head>
<meta charset="utf-8">
<title>Quillbrook Sound Rooms</title>
<link href="https://fonts.googleapis.com/css2?family=PT+Sans:ital,wght@0,400;0,700;1,400&family=Kreon:wght@400&family=Titillium+Web:ital,wght@1,400&display=swap" rel="stylesheet">
<style>
:root{
  --outside:#cbcbcb;
  --page:#353535;
  --header:#323232;
  --footer:#2f2f2f;
  --bottom:#272727;
  --band:#4a4a4a;
  --orange:#f37122;
  --orange-light:#f78f20;
  --text:#b4b4b4;
  --muted:#8c8c8c;
  --white:#f2f2f2;
  --line:#4d4d4d;
}
*{margin:0;padding:0;box-sizing:border-box}
html,body{width:960px;height:1200px;overflow:hidden}
body{background:var(--outside);font-family:"PT Sans",sans-serif;color:var(--text);position:relative}
.page{position:absolute;left:86px;top:0;width:795px;height:1200px;background:var(--page)}
.abs{position:absolute}
/* header */
.header{left:0;top:0;width:795px;height:56px;background:var(--header);border-bottom:1px solid #555}
.brand{left:87px;top:10px;display:flex;align-items:center;gap:8px;font-family:"PT Sans",sans-serif;font-weight:700;font-size:27px;color:#c8a43a}
.brand-mark{width:16px;height:16px;border-radius:50%;background:#c8a43a}
.nav{left:336px;top:0;display:flex;font-size:11px;color:var(--white)}
.nav a{color:var(--white);text-decoration:none;display:block;padding:21px 15px 0;height:56px}
.nav a.active{color:var(--orange);border-top:2px solid var(--orange);padding-top:19px}
/* slider */
.slider{left:0;top:56px;width:795px;height:280px;background:linear-gradient(90deg,#7a1414 0%,#9b1c1c 35%,#a42020 60%,#5e1b1b 100%)}
.slider-ceiling{left:0;top:0;width:795px;height:90px;background:linear-gradient(180deg,#d9b8a8,#b0483a 70%,rgba(160,40,30,0))}
.slide-title{left:84px;top:56px;width:330px;font-size:25px;line-height:29px;color:#fff}
.slide-sub{left:84px;top:119px;font-size:14px;color:var(--orange-light)}
.slide-body{left:84px;top:146px;width:280px;font-size:8px;line-height:13px;color:#fff}
.btn{left:84px;top:193px;width:132px;height:30px;background:linear-gradient(180deg,#f9b13a,#f08a1a);border:1px solid #ffc56a;color:#4a2a05;font-size:11px;display:flex;align-items:center;justify-content:center}
.arrow{width:38px;height:40px;background:rgba(40,20,20,.55);display:flex;align-items:center;justify-content:center}
/* features */
.feature{top:378px;width:195px}
.feature-head{display:flex;align-items:center;gap:10px;font-family:"Kreon",serif;font-size:14px;color:var(--white)}
.feature-icon{width:23px;height:23px;border-radius:50%;background:#c9c9c9;display:flex;align-items:center;justify-content:center}
.feature p{margin-top:11px;font-size:8px;line-height:13px;color:var(--text)}
.learn{margin-top:14px;text-align:right;font-size:7.5px;color:#e0e0e0}
.learn.on{color:var(--orange)}
/* section heading */
.sec-title{font-family:"Kreon",serif;font-size:13px;color:var(--white);display:flex;align-items:center;gap:10px;white-space:nowrap}
.sec-title::after{content:"";flex:1;height:3px;border-top:1px solid var(--line);border-bottom:1px solid var(--line)}
.thumb{top:568px;width:117px;height:90px}
.mini-arrow{width:19px;height:19px;background:#444;display:flex;align-items:center;justify-content:center}
.copy{font-size:8px;line-height:22px;color:var(--text)}
.quote{left:399px;top:758px;width:295px;height:97px;background:#4a4a4a;padding:14px 16px;font-style:italic;font-size:8px;line-height:13px;color:#a9a9a9}
.quote-tail{left:425px;top:855px}
.cite{left:432px;top:870px;font-size:8px;color:#b5b5b5}
.cite b{color:#ddd}
.call{left:0;top:940px;width:795px;text-align:center;font-family:"Titillium Web",sans-serif;font-style:italic;font-size:16.5px;color:#fff}
/* footer */
.band{left:0;top:967px;width:795px;height:6px;background:var(--band)}
.footer{left:0;top:973px;width:795px;height:189px;background:var(--footer)}
.f-title{font-size:12px;color:#fff}
.f-head{font-size:8px;font-weight:700;color:#ddd;letter-spacing:.2px}
.f-text{font-style:italic;font-size:8px;line-height:13px;color:#8a8a8a}
.post{font-size:8px;color:#cfcfcf;padding:6px 0 7px;border-bottom:1px solid #434343;width:140px}
.tweet{font-size:8px;line-height:13px;color:#8a8a8a;width:145px}
.tweet b{font-weight:400;color:#d0d0d0}
.gallery-grid{display:grid;grid-template-columns:repeat(4,33px);gap:3px}
.gallery-grid span{display:block;width:33px;height:34px;background:#e6e7e9}
.bottom{left:0;top:1162px;width:795px;height:38px;background:var(--bottom)}
.bottom-copy{left:84px;top:1176px;font-size:7px;color:#9a9a9a}
.social{display:flex;gap:15px;left:589px;top:1176px}
.social span{width:10px;height:10px;border-radius:50%;background:#555}
.tip{left:577px;top:1153px;background:#444;color:#ccc;font-size:6.5px;padding:2px 7px}
</style>
</head>
<body>
<div class="page">
  <header class="header abs">
    <div class="brand abs"><span class="brand-mark"></span>Quillbrook</div>
    <nav class="nav abs">
      <a class="active" href="#">Home</a><a href="#">Features</a><a href="#">Shortcodes</a><a href="#">Pages</a><a href="#">Portfolio</a><a href="#">Blog</a>
    </nav>
  </header>

  <section class="slider abs" role="img" aria-label="Photo of a red custom home theater room with a ceiling light, couch and projection screen">
    <div class="slider-ceiling abs"></div>
    <div class="slide-title abs">Custom Home Theaters and Media Rooms</div>
    <div class="slide-sub abs">An effective home theater showcases your</div>
    <div class="slide-body abs">Lid est laborum dolo rumes fugats untras. Et harums ser quidem rerum facilis dolores nemis omnis fugiats vitaes nemo minima rerums unsers sadips amets.</div>
    <div class="btn abs">READ MORE</div>
    <div class="arrow abs" style="left:2px;top:108px"><svg width="10" height="14"><path d="M8 1 2 7l6 6" stroke="#fff" stroke-width="2" fill="none"/></svg></div>
    <div class="arrow abs" style="left:754px;top:108px"><svg width="10" height="14"><path d="M2 1l6 6-6 6" stroke="#fff" stroke-width="2" fill="none"/></svg></div>
  </section>

  <div class="feature abs" style="left:84px">
    <div class="feature-head"><span class="feature-icon"><svg width="12" height="10"><rect x="1" y="1" width="10" height="6" fill="none" stroke="#444" stroke-width="1.5"/><rect x="0" y="8" width="12" height="1.5" fill="#444"/></svg></span>Responsive Design</div>
    <p>Lid est laborum dolo rumes fugats untras. Etharums ser quidem rerum facilis dolores nemis omnis fugats vitaes nemo minima rerums unsers sadips amets.</p>
    <div class="learn">Learn More &nbsp;›</div>
  </div>
  <div class="feature abs" style="left:292px">
    <div class="feature-head"><span class="feature-icon"><svg width="12" height="12"><path d="M2 6a4 4 0 0 1 7-2.5M10 6a4 4 0 0 1-7 2.5" stroke="#444" stroke-width="1.6" fill="none"/></svg></span>Awesome Sliders</div>
    <p>Lid est laborum dolo rumes fugats untras. Etharums ser quidem rerum facilis dolores nemis omnis fugats vitaes nemo minima rerums unsers sadips amets.</p>
    <div class="learn">Learn More &nbsp;›</div>
  </div>
  <div class="feature abs" style="left:500px">
    <div class="feature-head"><span class="feature-icon"><svg width="12" height="10"><rect x="1" y="1" width="10" height="8" fill="none" stroke="#444" stroke-width="1.5"/><path d="M4 1v8M8 1v8" stroke="#444"/></svg></span>Loaded With Options</div>
    <p>Lid est laborum dolo rumes fugats untras. Etharums ser quidem rerum facilis dolores nemis omnis fugats vitaes nemo minima rerums unsers sadips amets.</p>
    <div class="learn on">Learn More &nbsp;›</div>
  </div>

  <div class="sec-title abs" style="left:86px;top:534px;width:611px">Recent Work</div>
  <div class="mini-arrow abs" style="left:84px;top:595px"><svg width="6" height="8"><path d="M5 1 1 4l4 3" stroke="#ddd" fill="none"/></svg></div>
  <div class="mini-arrow abs" style="left:677px;top:595px"><svg width="6" height="8"><path d="M1 1l4 3-4 3" stroke="#ddd" fill="none"/></svg></div>
  <div class="thumb abs" style="left:123px;background:linear-gradient(135deg,#8a2a20,#c0563c,#6e1c17)" role="img" aria-label="Theater wall with decorative red panels"></div>
  <div class="thumb abs" style="left:261px;background:linear-gradient(180deg,#d8d0b8,#6a6250 60%,#2a2a2a)" role="img" aria-label="Home theater with rows of seats facing a screen"></div>
  <div class="thumb abs" style="left:400px;background:linear-gradient(135deg,#3a2a20,#1a1a1a 50%,#5a3030)" role="img" aria-label="Dark media room with space-themed panels"></div>
  <div class="thumb abs" style="left:539px;background:linear-gradient(135deg,#3a6ab0,#c8d0dc 50%,#b04020)" role="img" aria-label="Acoustic panels printed with a sports car"></div>

  <div class="sec-title abs" style="left:86px;top:721px;width:297px">Home Theater Design</div>
  <div class="copy abs" style="left:88px;top:741px;width:300px">In terms of design, your Home Theater is the most versatile room in your home.<br>Your options are limitless. You can compliment your existing home decor or you<br>can create a design that is completely different from the rest of your home.<br>If you enjoy exploring unique design opportunities, our decorative acoustic<br>panels can act as a canvas for your inspiration.<br><br>Mara Ellison created dozens of original artistic designs specifically for Home<br>Theater Interiors.</div>

  <div class="sec-title abs" style="left:397px;top:721px;width:297px">What Client’s Say</div>
  <div class="quote abs">“Neque porro quisquam est, qui dolorem ipsum quia dolor sit amet, consec tetur, adipisci velit, sed quia non numquam eius modi tempora incidunt utis labore et dolore magnam aliquam quaerat voluptatem. Ut enim ad minimas veniam, quis nostrum exercitationem ullam corporis suscipit laboriosam, nisi ut aliquid ex ea commodi consequatur slores amet untras vel illum qui.”</div>
  <svg class="quote-tail abs" width="14" height="9"><path d="M0 0h14L2 9z" fill="#4a4a4a"/></svg>
  <svg class="abs" style="left:399px;top:863px" width="18" height="18"><circle cx="9" cy="5" r="4" fill="#888"/><path d="M1 18c0-6 16-6 16 0z" fill="#888"/></svg>
  <div class="cite abs"><b>Sam Arden,</b> Arden Studio</div>

  <div class="call abs">Call Today (555-014-2290) To Discuss All Your Home Theater Design Options</div>

  <div class="band abs"></div>
  <footer class="footer abs">
    <div class="abs" style="left:84px;top:36px;width:135px">
      <div class="f-title">Home Theater Design</div>
      <div class="f-text" style="margin-top:8px">Lorem ipsum ex vix illud nonummy, novum tation et his. At vix scriptaset patrioque scribentur, at pro fugit erts verterem molestiae, sed et vivendo ali Lorem ipsum ex vix illud nonummy, novum tation et his. At vix scripta patrioque scribentur...</div>
    </div>
    <div class="abs" style="left:240px;top:36px">
      <div class="f-head">RECENT POSTS</div>
      <div style="margin-top:10px">
        <div class="post">Voluptas Sadips Ipsums Dolors Untra</div>
        <div class="post">Fugiats Litora Ultrices Ante Auctor</div>
        <div class="post">Sapien Litora Dolores Ultrices</div>
        <div class="post" style="border:0">Nemis Fugiats Voluptas Dolores Uns</div>
      </div>
    </div>
    <div class="abs" style="left:396px;top:36px">
      <div class="f-head">UPDATES</div>
      <div class="tweet" style="margin-top:16px;padding-bottom:14px;border-bottom:1px solid #434343"><b>@lumenfox</b> ! What an aweosme theme! We love it, tons of options and great design, thank you! :) <b>12 minutes ago</b></div>
      <div class="tweet" style="margin-top:14px"><b>@lumenfox</b> you’ve got to check this one out, very cool looking! <b>25 minutes ago</b></div>
    </div>
    <div class="abs" style="left:553px;top:36px">
      <div class="f-head">GALLERY</div>
      <div class="gallery-grid" style="margin-top:16px"><span></span><span></span><span></span><span></span><span></span><span></span><span></span><span></span></div>
    </div>
  </footer>
  <div class="bottom abs"></div>
  <div class="bottom-copy abs">Copyright 2015 Your Home Theater Design | &nbsp;All Rights Reserved</div>
  <div class="tip abs">Social</div>
  <div class="social abs"><span></span><span></span><span></span><span></span><span></span></div>
</div>
</body>
</html>
```